Specialty Coffee Company- Need Gift Card Design

We need a new design with our new logo for our gift card. Use attached logo. Can use white logo on dark background or our dark brown logo color on lighter background. Possibly have some sort of modern coffee related background. Only need front of card designed.
It Company

```html
<!DOCTYPE html>
<html lang="en">
<head>
<meta charset="utf-8">
<title>Corvella Gift Card – Front, Print Layout</title>
<link rel="stylesheet" href="https://fonts.googleapis.com/css2?family=Source+Sans+3:wght@400&family=Varela+Round&display=swap">
<style>
  :root {
    --page: #ffffff;
    --guide-red: #e8453c;
    --label-ink: #111111;
    --leader: #333333;
    --espresso: #5e3514;
    --espresso-glow: #7a4a26;
    --latte: #e0c6b6;
    --mark-light: #ffffff;
    --mark-dark: #4a2812;
  }
  html, body {
    margin: 0;
    padding: 0;
    overflow: hidden;
    background: var(--page);
  }
  .print-sheet {
    position: relative;
    width: 1200px;
    height: 1132px;
    overflow: hidden;
    background: var(--page);
  }
  .print-sheet svg {
    position: absolute;
    inset: 0;
    display: block;
  }
  .guide-label {
    font-family: "Source Sans 3", "Myriad Pro", Arial, sans-serif;
    font-size: 34px;
    fill: var(--label-ink);
  }
  .leader-line {
    stroke: var(--leader);
    stroke-width: 1.6;
  }
  .bleed-line, .cut-line, .safe-line {
    fill: none;
    stroke: var(--guide-red);
  }
  .bleed-line { stroke-width: 2.4; }
  .cut-line { stroke-width: 2.4; }
  .safe-line { stroke-width: 2.4; }
  .card-dark-fill { fill: url(#espressoGlow); }
  .card-light-fill { fill: var(--latte); }
  .brand-name {
    font-family: "Varela Round", "Nunito", sans-serif;
    font-size: 78px;
    letter-spacing: 1px;
  }
  .brand-name--light { fill: var(--mark-light); }
  .brand-name--dark { fill: var(--mark-dark); }
  .brand-dot--light { fill: var(--mark-light); }
  .brand-dot--dark { fill: var(--mark-dark); }
</style>
</head>
<body>
<main class="print-sheet">
  <svg width="1200" height="1132" viewBox="0 0 1200 1132" xmlns="http://www.w3.org/2000/svg" aria-label="Gift card front in two colour versions with bleed, cut and safe guides">
    <defs>
      <radialGradient id="espressoGlow" cx="0.45" cy="0.45" r="0.55">
        <stop offset="0" stop-color="var(--espresso-glow)"/>
        <stop offset="0.45" stop-color="var(--espresso)"/>
        <stop offset="1" stop-color="var(--espresso)"/>
      </radialGradient>
    </defs>

    <!-- Dark version -->
    <g class="card-version card-version--dark">
      <rect class="bleed-line" x="290" y="3" width="905" height="540" rx="24"/>
      <rect class="card-dark-fill" x="319" y="29" width="856" height="486"/>
      <rect class="cut-line" x="322" y="32" width="847" height="480" rx="32"/>
      <rect class="safe-line" x="351" y="61" width="786" height="422"/>

      <g class="brand-lockup">
        <circle class="brand-dot--light" cx="545" cy="258" r="26"/>
        <text class="brand-name brand-name--light" x="590" y="285">Corvella</text>
      </g>

      <g class="guide-labels">
        <text class="guide-label" x="13" y="76">Bleed</text>
        <line class="leader-line" x1="148" y1="60" x2="287" y2="60"/>
        <text class="guide-label" x="124" y="139">Cut</text>
        <line class="leader-line" x1="201" y1="127" x2="320" y2="127"/>
        <text class="guide-label" x="48" y="202">Safe</text>
        <line class="leader-line" x1="116" y1="190" x2="353" y2="190"/>
      </g>
    </g>

    <!-- Light version -->
    <g class="card-version card-version--light">
      <rect class="bleed-line" x="290" y="586" width="905" height="541" rx="24"/>
      <rect class="card-light-fill" x="319" y="615" width="856" height="486"/>
      <rect class="cut-line" x="322" y="615" width="847" height="483" rx="32"/>
      <rect class="safe-line" x="351" y="644" width="786" height="425"/>

      <g class="brand-lockup">
        <circle class="brand-dot--dark" cx="545" cy="848" r="26"/>
        <text class="brand-name brand-name--dark" x="590" y="875">Corvella</text>
      </g>

      <g class="guide-labels">
        <text class="guide-label" x="3" y="661">Bleed</text>
        <line class="leader-line" x1="148" y1="642" x2="290" y2="642"/>
        <text class="guide-label" x="113" y="724">Cut</text>
        <line class="leader-line" x1="201" y1="712" x2="320" y2="712"/>
        <text class="guide-label" x="35" y="788">Safe</text>
        <line class="leader-line" x1="121" y1="774" x2="353" y2="774"/>
      </g>
    </g>
  </svg>
</main>
</body>
</html>
```